table invoices in a modern format! (make it fun to look at!!)

Our has invoices that are shown to our clients. This is currently done in a normal table view, but its boring to look at and is not modern.
We would like to have a modern look and feel
it should ABSOLUTLY not be in table form.
Cards, graphs, pictures, whatever... should be fun and almost interactive.

the table file is how it current looks like.
the other two files were "ideas" to have a better representation
IT DOES NOT NEED TO LOOK LIKE THAT if you have a better idea please go for it.

secondary objective, the graphs/cards/whatever you design should be interactive, meaning I can "click on it" to pay a bill, or see more info.

Let me know if there are more questions!

```html
<!DOCTYPE html>
<html lang="en">
<head>
<meta charset="utf-8">
<title>Invoices – Year Overview</title>
<link href="https://fonts.googleapis.com/css2?family=Montserrat:wght@700&family=Roboto:wght@400;500;700&display=swap" rel="stylesheet">
<style>
  :root{
    --band:#e3f0fb;
    --row:#e3effa;
    --teal:#0a89a4;
    --green:#33a64a;
    --slate:#464a54;
    --amber:#fbbd2e;
    --red:#dc3545;
    --ink:#1e1f24;
    --muted:#a9abb0;
    --white:#ffffff;
  }
  *{box-sizing:border-box;margin:0;padding:0}
  html,body{width:1200px;height:914px;overflow:hidden;background:var(--white);font-family:"Roboto",sans-serif;color:var(--ink)}
  .canvas{position:relative;width:1200px;height:914px}

  .years{position:absolute;left:0;top:23px;width:1200px;height:47px;background:var(--band)}
  .year-tab{position:absolute;top:0;width:116px;height:47px;text-align:center;font-size:18px;font-weight:700;color:var(--muted);padding-top:17px;cursor:pointer}
  .year-tab::after{content:"";position:absolute;left:0;right:0;bottom:0;height:4px;border-radius:2px;background:var(--muted)}
  .year-tab.is-active{color:var(--ink)}
  .year-tab.is-active::after{background:#2e3038}
  .year-overview{position:absolute;left:1017px;top:23px;width:159px;height:47px;border-radius:6px;background:var(--slate);color:var(--white);font-weight:700;font-size:20px;display:flex;align-items:center;justify-content:center}

  .summary{position:absolute;left:0;top:83px;width:1200px;height:170px;background:var(--band)}
  .stat-card{position:absolute;top:19px;width:268px;height:126px;border-radius:32px;color:var(--white);cursor:pointer}
  .stat-card.payment{left:30px;background:var(--teal)}
  .stat-card.total{left:318px;background:var(--green)}
  .stat-card.balance{left:602px;background:var(--slate)}
  .stat-icon{position:absolute;left:33px;top:15px;width:32px;height:34px}
  .stat-title{position:absolute;left:70px;top:27px;font-family:"Montserrat",sans-serif;font-weight:700;font-size:21px;letter-spacing:.3px}
  .stat-amount{position:absolute;left:33px;top:66px;font-family:"Montserrat",sans-serif;font-weight:700;font-size:34px;letter-spacing:.5px}
  .move-wallet{position:absolute;left:1095px;top:122px;width:80px;height:24px;border-radius:5px;background:var(--slate);color:var(--white);font-size:8.5px;font-weight:700;display:flex;align-items:center;justify-content:center}

  .toolbar{position:absolute;left:0;top:263px;width:1200px;height:47px;background:var(--band)}
  .toolbar .refresh{position:absolute;left:40px;top:16px;width:13px;height:13px}
  .toolbar .select-all{position:absolute;left:59px;top:16px;width:13px;height:13px;border:1.3px solid #333;background:var(--white)}
  .toolbar .show-more{position:absolute;left:91px;top:13px;font-size:16px}

  .invoice{position:absolute;left:30px;width:1145px;height:46px;background:var(--row);box-shadow:0 3px 4px rgba(0,0,0,.14);cursor:pointer}
  .invoice .pick{position:absolute;left:12px;top:17px;width:12px;height:12px;border:1.2px solid #555;border-radius:3px;background:var(--white)}
  .cell{position:absolute;top:0;height:46px}
  .cell .head{height:24px;display:flex;align-items:center;justify-content:center;font-size:7px;font-weight:700;text-transform:uppercase;position:relative;padding-right:6px}
  .cell .head.chip{color:var(--white);font-weight:500}
  .cell .value{text-align:center;font-size:8.5px;margin-top:3px;text-transform:uppercase}
  .cell .value.strong{font-weight:700}
  .sort{position:absolute;right:6px;top:7px;width:5px;height:11px}
  .sort::before,.sort::after{content:"";position:absolute;left:0;border-left:2.5px solid transparent;border-right:2.5px solid transparent}
  .sort::before{top:0;border-bottom:5px solid var(--muted)}
  .sort::after{bottom:0;border-top:5px solid var(--muted)}
  .chip .sort::before{border-bottom-color:#2e3038}
  .chip .sort::after{border-top-color:#2e3038}
  .chip.red .sort::before,.chip.green.on-dark .sort::before{border-bottom-color:var(--white)}
  .chip.red .sort::after,.chip.green.on-dark .sort::after{border-top-color:var(--white)}
  .amber{background:var(--amber)}
  .green{background:var(--green)}
  .red{background:var(--red)}
  .pdf-tag{font-weight:700;margin-right:4px}
  .pdf-label{text-transform:none;font-weight:700;font-size:7px}

  .c-status{left:46px;width:107px}
  .c-month{left:153px;width:110px}
  .c-number{left:262px;width:110px}
  .c-option{left:378px;width:110px}
  .c-contract{left:492px;width:107px}
  .c-extra{left:599px;width:104px}
  .c-received{left:707px;width:110px}
  .c-wallet{left:817px;width:110px}
  .c-open{left:926px;width:107px}
  .c-days{left:1036px;width:104px}
</style>
</head>
<body>
<div class="canvas">

  <nav class="years">
    <div class="year-tab" style="left:30px">2019</div>
    <div class="year-tab is-active" style="left:149px">2020</div>
    <div class="year-tab" style="left:268px">2021</div>
    <div class="year-tab" style="left:387px">2022</div>
    <div class="year-tab" style="left:507px">2023</div>
  </nav>
  <div class="year-overview">Year Overview</div>

  <section class="summary">
    <div class="stat-card payment">
      <svg class="stat-icon" viewBox="0 0 32 34" fill="none" stroke="#fff" stroke-width="1.8">
        <path d="M6 12 L18 4 L26 12"/>
        <rect x="2" y="13" width="28" height="16" rx="1.5"/>
        <circle cx="16" cy="21" r="4.5"/>
        <circle cx="7" cy="21" r="1.2" fill="#fff"/>
        <circle cx="25" cy="21" r="1.2" fill="#fff"/>
      </svg>
      <div class="stat-title">PAYMENT</div>
      <div class="stat-amount">$ 10651.93</div>
    </div>
    <div class="stat-card total">
      <svg class="stat-icon" viewBox="0 0 32 34" fill="none" stroke="#fff" stroke-width="1.8">
        <path d="M3 2 L23 2 L23 32 L3 32 Z"/>
        <path d="M23 18 L29 18 L29 32 L23 32"/>
        <path d="M8 8 H18 M8 20 H18 M8 24 H18 M8 28 H15"/>
        <path d="M16 11 a3.5 3.5 0 1 0 0 5"/>
      </svg>
      <div class="stat-title">TOTAL PRICE</div>
      <div class="stat-amount">$ 10651.93</div>
    </div>
    <div class="stat-card balance">
      <svg class="stat-icon" viewBox="0 0 36 36" fill="none" stroke="#fff" stroke-width="1.8" style="left:22px;top:10px;width:38px;height:38px">
        <rect x="2" y="10" width="28" height="24" rx="4"/>
        <rect x="8" y="3" width="18" height="10" rx="2"/>
        <path d="M12 4 V12 M17 4 V12 M22 4 V12"/>
        <rect x="22" y="18" width="12" height="9" rx="2"/>
        <path d="M13 17 a4 4 0 1 0 0 8 M7 20 H12 M7 23 H12"/>
      </svg>
      <div class="stat-title">BALANCE</div>
      <div class="stat-amount">$ 10651.93</div>
    </div>
    <div class="move-wallet">Move To Wallet</div>
  </section>

  <div class="toolbar">
    <svg class="refresh" viewBox="0 0 14 14" fill="none" stroke="#222" stroke-width="1.7"><path d="M4 2.5 A5.5 5.5 0 1 0 8.5 1.8"/><path d="M8 0 L8.6 2 L6.5 3" /></svg>
    <span class="select-all"></span>
    <span class="show-more">Show More</span>
  </div>

  <!-- invoice rows -->
  <div class="invoice" style="top:328px">
    <span class="pick"></span>
    <div class="cell c-status"><div class="head chip amber">PAID<span class="sort"></span></div><div class="value">PARTIAL 225 DAYS LATE</div></div>
    <div class="cell c-month"><div class="head">MONTH<span class="sort"></span></div><div class="value">JAN 2019 ZML</div></div>
    <div class="cell c-number"><div class="head">NUMBER<span class="sort"></span></div><div class="value">TKZ19-0037</div></div>
    <div class="cell c-option"><div class="head"><span class="pdf-tag">PDF</span><span class="pdf-label">Payment Option</span><span class="sort"></span></div><div class="value">ACTUAL</div></div>
    <div class="cell c-contract"><div class="head chip green on-dark">CONTRACT PRICE<span class="sort"></span></div><div class="value">$1152.00</div></div>
    <div class="cell c-extra"><div class="head">EXTRA AFTER CREDITS<span class="sort"></span></div><div class="value">$141.18</div></div>
    <div class="cell c-received"><div class="head">PAYMENT RECEIVED<span class="sort"></span></div><div class="value">$1243.20</div></div>
    <div class="cell c-wallet"><div class="head">WALLET<span class="sort"></span></div><div class="value"></div></div>
    <div class="cell c-open"><div class="head chip red">OPEN BALANCE<span class="sort"></span></div><div class="value">$ -49.98</div></div>
    <div class="cell c-days"><div class="head">CONTRACT DAYS<span class="sort"></span></div><div class="value">12</div></div>
  </div>

  <div class="invoice" style="top:402px">
    <span class="pick"></span>
    <div class="cell c-status"><div class="head chip green">PAID<span class="sort"></span></div><div class="value">PARTIAL 225 DAYS LATE</div></div>
    <div class="cell c-month"><div class="head">MONTH<span class="sort"></span></div><div class="value">JAN 2019 ZML</div></div>
    <div class="cell c-number"><div class="head">NUMBER<span class="sort"></span></div><div class="value">TKZ19-0037</div></div>
    <div class="cell c-option"><div class="head"><span class="pdf-tag">PDF</span><span class="pdf-label">Payment Option</span><span class="sort"></span></div><div class="value">ACTUAL</div></div>
    <div class="cell c-contract"><div class="head chip green on-dark">CONTRACT PRICE<span class="sort"></span></div><div class="value">$1152.00</div></div>
    <div class="cell c-extra"><div class="head">EXTRA AFTER CREDITS<span class="sort"></span></div><div class="value">$141.18</div></div>
    <div class="cell c-received"><div class="head">PAYMENT RECEIVED<span class="sort"></span></div><div class="value">$1243.20</div></div>
    <div class="cell c-wallet"><div class="head">WALLET<span class="sort"></span></div><div class="value"></div></div>
    <div class="cell c-open"><div class="head chip green on-dark">OPEN BALANCE<span class="sort"></span></div><div class="value">$ -49.98</div></div>
    <div class="cell c-days"><div class="head">CONTRACT DAYS<span class="sort"></span></div><div class="value">12</div></div>
  </div>

  <div class="invoice" style="top:476px">
    <span class="pick"></span>
    <div class="cell c-status"><div class="head chip red">NOT PAID<span class="sort"></span></div><div class="value">PARTIAL 225 DAYS LATE</div></div>
    <div class="cell c-month"><div class="head">MONTH<span class="sort"></span></div><div class="value">JAN 2019 ZML</div></div>
    <div class="cell c-number"><div class="head">NUMBER<span class="sort"></span></div><div class="value">TKZ19-0037</div></div>
    <div class="cell c-option"><div class="head"><span class="pdf-tag">PDF</span><span class="pdf-label">Payment Option</span><span class="sort"></span></div><div class="value">ACTUAL</div></div>
    <div class="cell c-contract"><div class="head chip green on-dark">CONTRACT PRICE<span class="sort"></span></div><div class="value">$1152.00</div></div>
    <div class="cell c-extra"><div class="head">EXTRA AFTER CREDITS<span class="sort"></span></div><div class="value">$141.18</div></div>
    <div class="cell c-received"><div class="head">PAYMENT RECEIVED<span class="sort"></span></div><div class="value">$1243.20</div></div>
    <div class="cell c-wallet"><div class="head">WALLET<span class="sort"></span></div><div class="value"></div></div>
    <div class="cell c-open"><div class="head chip red">OPEN BALANCE<span class="sort"></span></div><div class="value">$ -49.98</div></div>
    <div class="cell c-days"><div class="head">CONTRACT DAYS<span class="sort"></span></div><div class="value">12</div></div>
  </div>

  <div class="invoice" style="top:549px">
    <span class="pick"></span>
    <div class="cell c-status"><div class="head chip amber">PAID<span class="sort"></span></div><div class="value">PARTIAL 225 DAYS LATE</div></div>
    <div class="cell c-month"><div class="head">MONTH<span class="sort"></span></div><div class="value">JAN 2019 ZML</div></div>
    <div class="cell c-number"><div class="head">NUMBER<span class="sort"></span></div><div class="value">TKZ19-0037</div></div>
    <div class="cell c-option"><div class="head"><span class="pdf-tag">PDF</span><span class="pdf-label">Payment Option</span><span class="sort"></span></div><div class="value">ACTUAL</div></div>
    <div class="cell c-contract"><div class="head chip green on-dark">CONTRACT PRICE<span class="sort"></span></div><div class="value">$1152.00</div></div>
    <div class="cell c-extra"><div class="head">EXTRA AFTER CREDITS<span class="sort"></span></div><div class="value">$141.18</div></div>
    <div class="cell c-received"><div class="head">PAYMENT RECEIVED<span class="sort"></span></div><div class="value">$1243.20</div></div>
    <div class="cell c-wallet"><div class="head">WALLET<span class="sort"></span></div><div class="value"></div></div>
    <div class="cell c-open"><div class="head chip green on-dark">OPEN BALANCE<span class="sort"></span></div><div class="value">$ -49.98</div></div>
    <div class="cell c-days"><div class="head">CONTRACT DAYS<span class="sort"></span></div><div class="value">12</div></div>
  </div>

  <div class="invoice" style="top:623px">
    <span class="pick"></span>
    <div class="cell c-status"><div class="head chip green">PAID<span class="sort"></span></div><div class="value">PARTIAL 225 DAYS LATE</div></div>
    <div class="cell c-month"><div class="head">MONTH<span class="sort"></span></div><div class="value">JAN 2019 ZML</div></div>
    <div class="cell c-number"><div class="head">NUMBER<span class="sort"></span></div><div class="value">TKZ19-0037</div></div>
    <div class="cell c-option"><div class="head"><span class="pdf-tag">PDF</span><span class="pdf-label">Payment Option</span><span class="sort"></span></div><div class="value">ACTUAL</div></div>
    <div class="cell c-contract"><div class="head chip green on-dark">CONTRACT PRICE<span class="sort"></span></div><div class="value">$1152.00</div></div>
    <div class="cell c-extra"><div class="head">EXTRA AFTER CREDITS<span class="sort"></span></div><div class="value">$141.18</div></div>
    <div class="cell c-received"><div class="head">PAYMENT RECEIVED<span class="sort"></span></div><div class="value">$1243.20</div></div>
    <div class="cell c-wallet"><div class="head">WALLET<span class="sort"></span></div><div class="value"></div></div>
    <div class="cell c-open"><div class="head chip red">OPEN BALANCE<span class="sort"></span></div><div class="value">$ -49.98</div></div>
    <div class="cell c-days"><div class="head">CONTRACT DAYS<span class="sort"></span></div><div class="value">12</div></div>
  </div>

  <div class="invoice" style="top:698px">
    <span class="pick"></span>
    <div class="cell c-status"><div class="head chip amber">PAID<span class="sort"></span></div><div class="value">PARTIAL 225 DAYS LATE</div></div>
    <div class="cell c-month"><div class="head">MONTH<span class="sort"></span></div><div class="value strong">JAN 2019 ZML</div></div>
    <div class="cell c-number"><div class="head">NUMBER<span class="sort"></span></div><div class="value">TKZ19-0037</div></div>
    <div class="cell c-option"><div class="head"><span class="pdf-tag">PDF</span><span class="pdf-label">Payment Option</span><span class="sort"></span></div><div class="value">ACTUAL</div></div>
    <div class="cell c-contract"><div class="head chip green on-dark">CONTRACT PRICE<span class="sort"></span></div><div class="value">$1152.00</div></div>
    <div class="cell c-extra"><div class="head">EXTRA AFTER CREDITS<span class="sort"></span></div><div class="value">$141.18</div></div>
    <div class="cell c-received"><div class="head">PAYMENT RECEIVED<span class="sort"></span></div><div class="value">$1243.20</div></div>
    <div class="cell c-wallet"><div class="head">WALLET<span class="sort"></span></div><div class="value"></div></div>
    <div class="cell c-open"><div class="head chip green on-dark">OPEN BALANCE<span class="sort"></span></div><div class="value">$ -49.98</div></div>
    <div class="cell c-days"><div class="head">CONTRACT DAYS<span class="sort"></span></div><div class="value">12</div></div>
  </div>

  <div class="invoice" style="top:771px">
    <span class="pick"></span>
    <div class="cell c-status"><div class="head chip green">PAID<span class="sort"></span></div><div class="value">PARTIAL 225 DAYS LATE</div></div>
    <div class="cell c-month"><div class="head">MONTH<span class="sort"></span></div><div class="value">JAN 2019 ZML</div></div>
    <div class="cell c-number"><div class="head">NUMBER<span class="sort"></span></div><div class="value">TKZ19-0037</div></div>
    <div class="cell c-option"><div class="head"><span class="pdf-tag">PDF</span><span class="pdf-label">Payment Option</span><span class="sort"></span></div><div class="value">ACTUAL</div></div>
    <div class="cell c-contract"><div class="head chip green on-dark">CONTRACT PRICE<span class="sort"></span></div><div class="value">$1152.00</div></div>
    <div class="cell c-extra"><div class="head">EXTRA AFTER CREDITS<span class="sort"></span></div><div class="value">$141.18</div></div>
    <div class="cell c-received"><div class="head">PAYMENT RECEIVED<span class="sort"></span></div><div class="value">$1243.20</div></div>
    <div class="cell c-wallet"><div class="head">WALLET<span class="sort"></span></div><div class="value"></div></div>
    <div class="cell c-open"><div class="head chip red">OPEN BALANCE<span class="sort"></span></div><div class="value">$ -49.98</div></div>
    <div class="cell c-days"><div class="head">CONTRACT DAYS<span class="sort"></span></div><div class="value">12</div></div>
  </div>

  <div class="invoice" style="top:845px">
    <span class="pick"></span>
    <div class="cell c-status"><div class="head chip red">NOT PAID<span class="sort"></span></div><div class="value">PARTIAL 225 DAYS LATE</div></div>
    <div class="cell c-month"><div class="head">MONTH<span class="sort"></span></div><div class="value">JAN 2019 ZML</div></div>
    <div class="cell c-number"><div class="head">NUMBER<span class="sort"></span></div><div class="value">TKZ19-0037</div></div>
    <div class="cell c-option"><div class="head"><span class="pdf-tag">PDF</span><span class="pdf-label">Payment Option</span><span class="sort"></span></div><div class="value">ACTUAL</div></div>
    <div class="cell c-contract"><div class="head chip green on-dark">CONTRACT PRICE<span class="sort"></span></div><div class="value">$1152.00</div></div>
    <div class="cell c-extra"><div class="head">EXTRA AFTER CREDITS<span class="sort"></span></div><div class="value">$141.18</div></div>
    <div class="cell c-received"><div class="head">PAYMENT RECEIVED<span class="sort"></span></div><div class="value">$1243.20</div></div>
    <div class="cell c-wallet"><div class="head">WALLET<span class="sort"></span></div><div class="value"></div></div>
    <div class="cell c-open"><div class="head chip red">OPEN BALANCE<span class="sort"></span></div><div class="value">$ -49.98</div></div>
    <div class="cell c-days"><div class="head">CONTRACT DAYS<span class="sort"></span></div><div class="value">12</div></div>
  </div>

</div>
</body>
</html>
```